A Leisure SPA Plaza Hotel needs Creative VIP Cards Design

We need VIP Cards Design for a SPA Plaza Hotel, This leisure SPA plaza hotel have multiple sub projects, such as leisure hotel room, large buffet restaurant, swimming pool, theatrical performances, sauna bath, massage, SPA, Tea bar, 3D cinema, KTV rooms, chess room, Internet cafes , art appreciation, children's Castle, Korean geothermal, table tennis, billiard room, GYM and other entertainments.
We need Three creative VIP Card design for 3 different level:
1. Golden Card
2. Platinum Card
3. Diamond Card
Attached, Please find the LOGO file and some sample, we new design with much better look than those samples.

```html
<!DOCTYPE html>
<html lang="en">
<head>
<meta charset="utf-8">
<title>VIP Membership Cards – Gold, Platinum, Diamond</title>
<link rel="stylesheet" href="https://fonts.googleapis.com/css2?family=Josefin+Sans:wght@100;300&family=Arimo:wght@400&family=Noto+Sans+SC:wght@400;700&display=swap">
<style>
  :root {
    --page-bg: #ffffff;
    --card-dark: #242223;
    --card-black: #000000;
    --glow: #ffffff;
    --gold-ink: #8d7c12;
    --platinum-ink: #e9eeec;
    --diamond-ink: #111111;
    --logo-ink: #1e1c1d;
    --logo-sub: #4a4849;
    --back-text: #ffffff;
    --sign-strip: #ffffff;
    --gold-label: #7d6f1a;
    --platinum-label: #ffffff;
    --diamond-label: #222222;
  }
  html, body {
    margin: 0;
    width: 1200px;
    height: 1200px;
    overflow: hidden;
    background: var(--page-bg);
  }
  .sheet {
    position: relative;
    width: 1200px;
    height: 1200px;
  }
  .card {
    position: absolute;
    width: 480px;
    height: 300px;
    border-radius: 18px;
    overflow: hidden;
    box-shadow: 0 10px 18px rgba(0,0,0,0.35), 0 2px 4px rgba(0,0,0,0.2);
    background: var(--card-dark);
  }
  .card--front { left: 60px; }
  .card--back  { left: 660px; background: var(--card-black); }
  .row-gold     { top: 60px; }
  .row-platinum { top: 450px; }
  .row-diamond  { top: 840px; }

  .card__art {
    position: absolute;
    inset: 0;
    width: 480px;
    height: 300px;
  }

  /* Front */
  .vip-mark {
    position: absolute;
    left: 38px;
    top: 68px;
    margin: 0;
    font-family: "Josefin Sans", sans-serif;
    font-weight: 100;
    font-size: 122px;
    line-height: 1;
    letter-spacing: -2px;
  }
  .tier-name {
    position: absolute;
    left: 0;
    width: 290px;
    top: 200px;
    text-align: center;
    font-family: "Josefin Sans", sans-serif;
    font-weight: 300;
    font-size: 25px;
    letter-spacing: -0.5px;
    text-transform: uppercase;
  }
  .card--gold .vip-mark, .card--gold .tier-name { color: var(--gold-ink); }
  .card--platinum .vip-mark, .card--platinum .tier-name { color: var(--platinum-ink); }
  .card--diamond .vip-mark, .card--diamond .tier-name { color: var(--diamond-ink); }

  .brand {
    position: absolute;
    left: 296px;
    width: 172px;
    top: 160px;
    text-align: center;
    color: var(--logo-ink);
  }
  .brand__cn {
    font-family: "Noto Sans SC", sans-serif;
    font-weight: 700;
    font-size: 22px;
    line-height: 1;
    letter-spacing: 1px;
  }
  .brand__en {
    margin-top: 6px;
    font-family: "Josefin Sans", sans-serif;
    font-weight: 300;
    font-size: 13px;
    color: var(--logo-sub);
  }

  /* Back */
  .sign-strip {
    position: absolute;
    left: 19px;
    top: 32px;
    width: 442px;
    height: 30px;
    background: var(--sign-strip);
  }
  .sign-label {
    position: absolute;
    left: 0;
    width: 480px;
    top: 74px;
    text-align: center;
  }
  .sign-label__en {
    font-family: "Josefin Sans", sans-serif;
    font-weight: 300;
    font-size: 21px;
    letter-spacing: -0.5px;
  }
  .sign-label__cn {
    margin-top: 4px;
    font-family: "Noto Sans SC", sans-serif;
    font-weight: 400;
    font-size: 21px;
    letter-spacing: 1px;
  }
  .card--gold .sign-label { color: var(--gold-label); }
  .card--platinum .sign-label { color: var(--platinum-label); }
  .card--diamond .sign-label { color: var(--diamond-label); }

  .terms {
    position: absolute;
    left: 0;
    width: 480px;
    top: 190px;
    text-align: center;
    color: var(--back-text);
    font-family: "Arimo", sans-serif;
    font-size: 11.5px;
    line-height: 14px;
  }
  .terms p { margin: 0 0 26px; }
</style>
</head>
<body>
<main class="sheet">

  <!-- Gold -->
  <article class="card card--front card--gold row-gold">
    <svg class="card__art" viewBox="0 0 480 300" role="img" aria-label="Gold metallic panel with curved rim">
      <defs>
        <linearGradient id="gold-face" x1="0" y1="0" x2="0" y2="1">
          <stop offset="0" stop-color="#c6a600"/>
          <stop offset="0.45" stop-color="#ffdc00"/>
          <stop offset="1" stop-color="#b79c00"/>
        </linearGradient>
        <radialGradient id="gold-glow" cx="380" cy="150" r="110" gradientUnits="userSpaceOnUse">
          <stop offset="0.25" stop-color="#ffffff"/>
          <stop offset="1" stop-color="#242223"/>
        </radialGradient>
      </defs>
      <rect width="480" height="300" fill="#242223"/>
      <circle cx="380" cy="150" r="110" fill="url(#gold-glow)"/>
      <path d="M0 0 H236 Q378 150 226 300 H0 Z" fill="#8a7b2c"/>
      <path d="M0 0 H216 Q354 150 208 300 H0 Z" fill="url(#gold-face)"/>
    </svg>
    <h2 class="vip-mark">VIP</h2>
    <div class="tier-name">Gold Member</div>
    <div class="brand">
      <div class="brand__cn">晴湾休闲广场</div>
      <div class="brand__en">Sunmere Leisure Plaza</div>
    </div>
  </article>

  <article class="card card--back card--gold row-gold">
    <svg class="card__art" viewBox="0 0 480 300" aria-hidden="true">
      <defs>
        <linearGradient id="gold-band" x1="0" y1="0" x2="0" y2="1">
          <stop offset="0" stop-color="#b89c00"/>
          <stop offset="0.5" stop-color="#ffdc00"/>
          <stop offset="1" stop-color="#c9aa00"/>
        </linearGradient>
      </defs>
      <rect width="480" height="174" fill="url(#gold-band)"/>
      <rect y="138" width="480" height="20" fill="#8a7b3a"/>
      <rect y="158" width="480" height="16" fill="#c9a800"/>
    </svg>
    <div class="sign-strip"></div>
    <div class="sign-label">
      <div class="sign-label__en">AUTHORIZED SIGNITURE</div>
      <div class="sign-label__cn">授權的簽名</div>
    </div>
    <div class="terms">
      <p>PLEASE SHOW YOUR MEMBERSHIP CARD WHEN CHECKING OUT</p>
      <p>SIGNITURE AND USE OF THIS CARD CONFIRMS THE ACCEPTANCE<br>OF THE TERMS AND CONDITIONS OF MEMBERSHIPS</p>
    </div>
  </article>

  <!-- Platinum -->
  <article class="card card--front card--platinum row-platinum">
    <svg class="card__art" viewBox="0 0 480 300" role="img" aria-label="Platinum metallic panel with curved rim">
      <defs>
        <linearGradient id="plat-face" x1="0" y1="0" x2="0" y2="1">
          <stop offset="0" stop-color="#74797a"/>
          <stop offset="0.5" stop-color="#b2bebb"/>
          <stop offset="1" stop-color="#7f8b89"/>
        </linearGradient>
        <radialGradient id="plat-glow" cx="380" cy="150" r="110" gradientUnits="userSpaceOnUse">
          <stop offset="0.25" stop-color="#ffffff"/>
          <stop offset="1" stop-color="#242223"/>
        </radialGradient>
      </defs>
      <rect width="480" height="300" fill="#242223"/>
      <circle cx="380" cy="150" r="110" fill="url(#plat-glow)"/>
      <path d="M0 0 H236 Q378 150 226 300 H0 Z" fill="#c7d2cf"/>
      <path d="M0 0 H216 Q354 150 208 300 H0 Z" fill="url(#plat-face)"/>
    </svg>
    <h2 class="vip-mark">VIP</h2>
    <div class="tier-name">Platnium Member</div>
    <div class="brand">
      <div class="brand__cn">晴湾休闲广场</div>
      <div class="brand__en">Sunmere Leisure Plaza</div>
    </div>
  </article>

  <article class="card card--back card--platinum row-platinum">
    <svg class="card__art" viewBox="0 0 480 300" aria-hidden="true">
      <defs>
        <linearGradient id="plat-band" x1="0" y1="0" x2="0" y2="1">
          <stop offset="0" stop-color="#7c8282"/>
          <stop offset="0.5" stop-color="#b3c0bc"/>
          <stop offset="1" stop-color="#7d8987"/>
        </linearGradient>
      </defs>
      <rect width="480" height="174" fill="url(#plat-band)"/>
      <rect y="138" width="480" height="20" fill="#545d60"/>
      <rect y="158" width="480" height="16" fill="#b9c5c1"/>
    </svg>
    <div class="sign-strip"></div>
    <div class="sign-label">
      <div class="sign-label__en">AUTHORIZED SIGNITURE</div>
      <div class="sign-label__cn">授權的簽名</div>
    </div>
    <div class="terms">
      <p>PLEASE SHOW YOUR MEMBERSHIP CARD WHEN CHECKING OUT</p>
      <p>SIGNITURE AND USE OF THIS CARD CONFIRMS THE ACCEPTANCE<br>OF THE TERMS AND CONDITIONS OF MEMBERSHIPS</p>
    </div>
  </article>

  <!-- Diamond -->
  <article class="card card--front card--diamond row-diamond">
    <svg class="card__art" viewBox="0 0 480 300" role="img" aria-label="Icy faceted diamond surface panel with curved rim">
      <defs>
        <linearGradient id="dia-face" x1="0" y1="0" x2="1" y2="1">
          <stop offset="0" stop-color="#eef2f4"/>
          <stop offset="0.5" stop-color="#d2e4ef"/>
          <stop offset="1" stop-color="#f2f5f6"/>
        </linearGradient>
        <radialGradient id="dia-glow" cx="380" cy="150" r="110" gradientUnits="userSpaceOnUse">
          <stop offset="0.25" stop-color="#ffffff"/>
          <stop offset="1" stop-color="#242223"/>
        </radialGradient>
      </defs>
      <rect width="480" height="300" fill="#242223"/>
      <circle cx="380" cy="150" r="110" fill="url(#dia-glow)"/>
      <path d="M0 0 H236 Q378 150 226 300 H0 Z" fill="#f4f7f8"/>
      <path d="M0 0 H216 Q354 150 208 300 H0 Z" fill="url(#dia-face)"/>
    </svg>
    <h2 class="vip-mark">VIP</h2>
    <div class="tier-name">Diamond Member</div>
    <div class="brand">
      <div class="brand__cn">晴湾休闲广场</div>
      <div class="brand__en">Sunmere Leisure Plaza</div>
    </div>
  </article>

  <article class="card card--back card--diamond row-diamond">
    <svg class="card__art" viewBox="0 0 480 300" role="img" aria-label="Icy faceted diamond surface band">
      <defs>
        <linearGradient id="dia-band" x1="0" y1="0" x2="1" y2="1">
          <stop offset="0" stop-color="#d6e7f1"/>
          <stop offset="0.5" stop-color="#eef2f4"/>
          <stop offset="1" stop-color="#d9e8f1"/>
        </linearGradient>
      </defs>
      <rect width="480" height="174" fill="url(#dia-band)"/>
      <rect y="138" width="480" height="20" fill="#dbe9f2"/>
      <rect y="158" width="480" height="16" fill="#a9d0ec"/>
    </svg>
    <div class="sign-strip"></div>
    <div class="sign-label">
      <div class="sign-label__en">AUTHORIZED SIGNITURE</div>
      <div class="sign-label__cn">授權的簽名</div>
    </div>
    <div class="terms">
      <p>PLEASE SHOW YOUR MEMBERSHIP CARD WHEN CHECKING OUT</p>
      <p>SIGNITURE AND USE OF THIS CARD CONFIRMS THE ACCEPTANCE<br>OF THE TERMS AND CONDITIONS OF MEMBERSHIPS</p>
    </div>
  </article>

</main>
</body>
</html>
```